Diagram of Tallowmere’s history for website

This project is to design the attached diagram along the lines of the attached image but in our branding - style guide attached. The diagram will be going on the Tallowmere website - www.tallowmere.au.

```html
<!DOCTYPE html>
<html lang="en">
<head>
<meta charset="utf-8">
<title>Tallowmere History Timeline</title>
<link rel="stylesheet" href="https://fonts.googleapis.com/css2?family=Poppins:wght@400;500;600&display=swap">
<style>
  :root {
    --peach: #d4ac96;
    --green: #6c8c72;
    --slate: #7fa0a6;
    --desc-slate: #7d9a9e;
    --desc-green: #6f8f78;
    --bg: #ffffff;
  }
  html, body {
    margin: 0;
    padding: 0;
    width: 1200px;
    height: 675px;
    overflow: hidden;
    background: var(--bg);
  }
  .timeline {
    display: block;
    width: 1200px;
    height: 675px;
    font-family: "Poppins", sans-serif;
  }
  .chevron--peach { fill: var(--peach); }
  .chevron--green { fill: var(--green); }
  .chevron--slate { fill: var(--slate); }
  .year-label {
    fill: #ffffff;
    font-size: 64px;
    font-weight: 500;
    letter-spacing: 6px;
    text-anchor: middle;
  }
  .connector { fill: none; stroke-width: 2.5; }
  .connector--peach { stroke: var(--peach); }
  .connector--green { stroke: var(--green); }
  .connector--slate { stroke: var(--slate); }
  .node--peach { fill: var(--peach); }
  .node--green { fill: var(--green); }
  .node--slate { fill: var(--slate); }
  .event-title { font-size: 35px; font-weight: 600; }
  .event-title--peach { fill: var(--peach); }
  .event-title--green { fill: var(--green); }
  .event-title--slate { fill: var(--slate); }
  .event-desc { font-size: 20px; font-weight: 400; fill: var(--desc-slate); }
  .event-desc--green { fill: var(--desc-green); }
  .align-end { text-anchor: end; }
</style>
</head>
<body>
<svg class="timeline" viewBox="0 0 1920 1080" role="img" aria-label="Tallowmere history timeline 2017 to 2023">
  <g class="year-band">
    <path class="chevron--peach" d="M73 481H325L360 527L325 573H73L108 527Z"/>
    <text class="year-label" x="216" y="550">2017</text>
    <path class="chevron--green" d="M370 481H622L657 527L622 573H370L405 527Z"/>
    <text class="year-label" x="513" y="550">2018</text>
    <path class="chevron--slate" d="M667 481H919L954 527L919 573H667L702 527Z"/>
    <text class="year-label" x="810" y="550">2019</text>
    <path class="chevron--peach" d="M964 481H1216L1251 527L1216 573H964L999 527Z"/>
    <text class="year-label" x="1107" y="550">2021</text>
    <path class="chevron--green" d="M1261 481H1513L1548 527L1513 573H1261L1296 527Z"/>
    <text class="year-label" x="1404" y="550">2022</text>
    <path class="chevron--slate" d="M1558 481H1810L1845 527L1810 573H1558L1593 527Z"/>
    <text class="year-label" x="1701" y="550">2023</text>
  </g>

  <g class="milestone milestone--2017">
    <path class="connector connector--peach" d="M199 177V481M199 366H264"/>
    <circle class="node--peach" cx="199" cy="177" r="5"/>
    <circle class="node--peach" cx="264" cy="366" r="5"/>
    <text class="event-title event-title--peach" x="233" y="190">Tallowmere Commences</text>
    <text class="event-desc">
      <tspan x="238" y="217">Maren started the business with 25</tspan>
      <tspan x="238" y="241">years' experience working for</tspan>
      <tspan x="238" y="265">government&amp;non- government</tspan>
      <tspan x="238" y="289">disability &amp; community services. Our</tspan>
      <tspan x="238" y="313">first office is in Larkfield</tspan>
    </text>
    <text class="event-title event-title--peach" x="288" y="379">Tallowmere Commences</text>
    <text class="event-desc">
      <tspan x="293" y="408">Tallowmere becomes a NCSS</tspan>
      <tspan x="293" y="432">Registered provider</tspan>
    </text>
  </g>

  <g class="milestone milestone--2018">
    <path class="connector connector--green" d="M502 573V690"/>
    <circle class="node--green" cx="502" cy="690" r="5"/>
    <text class="event-title event-title--green align-end" x="482" y="698">Clinic Expansion</text>
    <text class="event-desc align-end">
      <tspan x="482" y="728">Tallowmere moves to</tspan>
      <tspan x="482" y="752">Elmsworth due to further</tspan>
      <tspan x="482" y="776">growth &amp; expansion</tspan>
    </text>
  </g>

  <g class="milestone milestone--2019">
    <path class="connector connector--slate" d="M799 481V366H860"/>
    <circle class="node--slate" cx="860" cy="366" r="5"/>
    <text class="event-title event-title--slate" x="884" y="379">Move to Elmsworth</text>
    <text class="event-desc">
      <tspan x="884" y="408">Tallowmere moves to Elmsworth due to</tspan>
      <tspan x="884" y="432">further growth &amp; expansion</tspan>
    </text>
  </g>

  <g class="milestone milestone--2021">
    <path class="connector connector--peach" d="M1067 573V690H1042"/>
    <circle class="node--peach" cx="1042" cy="690" r="5"/>
    <text class="event-title event-title--peach align-end" x="1013" y="698">Move to Elmsworth</text>
    <text class="event-desc align-end">
      <tspan x="1013" y="729">Tallowmere becomes a accredited</tspan>
      <tspan x="1013" y="753">Fair Enterprise having met the highest</tspan>
      <tspan x="1013" y="777">standards of environmental, social &amp;</tspan>
      <tspan x="1013" y="801">community performance</tspan>
    </text>
  </g>

  <g class="milestone milestone--2022">
    <path class="connector connector--green" d="M1405 481V179M1338 179H1480M1405 319H1480"/>
    <circle class="node--green" cx="1338" cy="179" r="5"/>
    <circle class="node--green" cx="1480" cy="179" r="5"/>
    <circle class="node--green" cx="1480" cy="319" r="5"/>
    <text class="event-title event-title--green align-end" x="1315" y="190">Kestrel Best of Business</text>
    <text class="event-desc align-end">
      <tspan x="1313" y="221">Tallowmere moves to Elmsworth due to</tspan>
      <tspan x="1313" y="245">further growth &amp; expansion</tspan>
    </text>
    <text class="event-title event-title--green" x="1498" y="190">Move to Harlow</text>
    <text class="event-desc event-desc--green">
      <tspan x="1498" y="219">Tallowmere moves to a larger</tspan>
      <tspan x="1498" y="243">premises in Harlow</tspan>
    </text>
    <text class="event-title event-title--green" x="1498" y="330">Partnerships</text>
    <text class="event-desc event-desc--green">
      <tspan x="1498" y="359">Partnerships established with</tspan>
      <tspan x="1498" y="383">Bayside School for Children with</tspan>
      <tspan x="1498" y="407">Disability &amp; Wattle Path Centre</tspan>
      <tspan x="1498" y="431">(Eastbrook University)</tspan>
    </text>
  </g>

  <g class="milestone milestone--2023">
    <path class="connector connector--slate" d="M1735 573V950M1686 686H1735M1686 777H1735M1686 864H1735M1686 950H1735"/>
    <circle class="node--slate" cx="1686" cy="686" r="5"/>
    <circle class="node--slate" cx="1686" cy="777" r="5"/>
    <circle class="node--slate" cx="1686" cy="864" r="5"/>
    <circle class="node--slate" cx="1686" cy="950" r="5"/>
    <text class="event-title event-title--slate align-end" x="1666" y="698">Community Inclusion Plan (CIP)</text>
    <text class="event-desc align-end" x="1666" y="732">Tallowmere’s Stage One CIP developed &amp;endorsed</text>
    <text class="event-title event-title--peach align-end" x="1663" y="789">Client Advisory Group</text>
    <text class="event-desc align-end" x="1663" y="821">Tallowmere’s Client Advisory Group commences</text>
    <text class="event-title event-title--slate align-end" x="1665" y="873">E-Learning Platform</text>
    <text class="event-desc align-end" x="1663" y="900">Tallowmere e-learning  platform launched</text>
    <text class="event-title event-title--peach align-end" x="1665" y="960">Pride Seal</text>
    <text class="event-desc align-end">
      <tspan x="1665" y="989">Tallowmere achieves Pride</tspan>
      <tspan x="1665" y="1013">Seal  accreditation</tspan>
    </text>
  </g>
</svg>
</body>
</html>
```